Technology Ideation/Innovation Consultant-One Page (for now) Site Reflective Of Its Focus.

Based in Tampa, Florida...I offer my consulting services, along with my extensive network of companies and technologies, to people that are looking for new, novel, and innovative applications for their technology and/or companies & governmental agencies to identify solutions to their Existing Challenges and Future Needs. I then Identify Connections and/or Solutions between technologies and set up collaborations between the parties. I also run a Forum that allows people to present new, novel, and innovative technologies and capabilities to a broad audience for ideation and collaboration.

Logo Text

Quantel Brightforge LLC

Coding

Coded - Design and coding required

```html
<!DOCTYPE html>
<html lang="en">
<head>
<meta charset="utf-8">
<title>Quantel Brightforge LLC</title>
<link href="https://fonts.googleapis.com/css2?family=Playfair+Display:wght@700&family=Poppins:wght@400;500;600&display=swap" rel="stylesheet">
<style>
:root{
  --blue:#0a6dc2;
  --blue-dark:#075aa3;
  --yellow:#f8d200;
  --pale:#f4f8fc;
  --wave:#dbe9f6;
  --ink:#2b2b2b;
  --grey:#555;
  --white:#fff;
}
*{margin:0;padding:0;box-sizing:border-box}
html,body{width:1200px;height:3921px;overflow:hidden;background:var(--white)}
body{position:relative;font-family:"Poppins",sans-serif;color:var(--ink)}
.abs{position:absolute}
.serif{font-family:"Playfair Display",serif;font-weight:700}
.brand{font-family:"Poppins",sans-serif;font-weight:600;color:var(--blue);font-size:21px;line-height:1.2}
.nav a{position:absolute;top:36px;font-size:15px;color:var(--ink);text-decoration:none}
.btn{display:flex;align-items:center;justify-content:center;gap:14px;font-size:15px;font-weight:500}
.btn .dot{width:20px;height:20px;border-radius:50%;display:flex;align-items:center;justify-content:center}
.btn-blue{background:var(--blue);color:var(--white)}
.btn-blue .dot{background:var(--yellow)}
.btn-yellow{background:var(--yellow);color:var(--blue)}
.btn-yellow .dot{background:var(--blue)}
.kicker{color:var(--yellow);text-align:center;width:1200px;left:0;font-size:26px}
.title{color:var(--blue);text-align:center;width:1200px;left:0;font-size:46px}
.lead{width:1200px;left:0;text-align:center;font-size:16px;color:var(--grey);line-height:26px}
.service{position:absolute;width:180px;text-align:center}
.service .ring{width:136px;height:136px;margin:0 auto;border-radius:50%;border:3px solid var(--blue);padding:6px}
.service .disc{width:100%;height:100%;border-radius:50%;background:var(--blue);display:flex;align-items:center;justify-content:center}
.service p{margin-top:16px;color:var(--blue);font-weight:600;font-size:19px}
.reason{position:absolute;left:84px;width:520px;display:flex;gap:28px}
.reason .bulb{width:92px;height:92px;border-radius:50%;border:3px solid #f7e98a;display:flex;align-items:center;justify-content:center;flex:none}
.reason h3{font-size:21px;font-weight:500;margin-top:4px;color:var(--ink)}
.reason p{font-size:15px;color:var(--grey);line-height:21px}
.info{position:absolute;left:94px;display:flex;gap:14px;align-items:center;font-size:15px;line-height:19px;color:var(--ink)}
.info .ic{width:32px;height:32px;border-radius:50%;background:var(--blue);display:flex;align-items:center;justify-content:center;flex:none}
.field{position:absolute;font-size:15px;color:var(--grey)}
.rule{position:absolute;left:592px;width:523px;height:1px;background:#9aa9b8}
.foot a{position:absolute;top:3776px;color:var(--white);font-size:16px;text-decoration:none}
.foot .sep{position:absolute;top:3776px;color:#9fc4e8;font-size:16px}
.social{position:absolute;top:3769px;width:34px;height:34px;border:2px solid var(--white);border-radius:50%}
</style>
</head>
<body>

<!-- Header -->
<div class="abs brand" style="left:85px;top:40px;width:200px">Quantel<br>Brightforge LLC</div>
<nav class="nav">
  <a style="left:586px">Home</a>
  <a style="left:683px">About us</a>
  <a style="left:806px">Services</a>
  <a style="left:925px">Blog</a>
  <a style="left:1018px">Contact Us</a>
</nav>

<!-- Hero -->
<svg class="abs" style="left:0;top:600px" width="1200" height="230" viewBox="0 0 1200 230">
  <path d="M0 90 C120 40 260 20 380 50 C560 100 700 220 900 200 C1060 185 1150 120 1200 80 L1200 230 L0 230Z" fill="var(--wave)"/>
  <path d="M0 120 C140 70 280 55 400 80 C580 120 720 230 920 215 C1070 205 1150 150 1200 120 L1200 230 L0 230Z" fill="var(--pale)"/>
</svg>
<div class="abs" style="left:0;top:760px;width:1200px;height:545px;background:var(--pale)"></div>

<div class="abs serif" style="left:85px;top:222px;font-size:40px;color:var(--yellow)">Welcome to</div>
<div class="abs serif" style="left:85px;top:272px;font-size:45px;color:var(--blue)">Quantel Brightforge LLC</div>
<p class="abs" style="left:85px;top:352px;width:450px;font-size:16px;line-height:23px;color:var(--grey)">Lorem ipsum dolor sit amet, consectetur adipiscing elised do eiusmod tempor ncididunt ut labore et dolo</p>
<div class="abs btn btn-blue" style="left:85px;top:428px;width:189px;height:61px">Learn More <span class="dot"><svg width="8" height="8" viewBox="0 0 8 8"><path d="M2 1l3 3-3 3" stroke="#fff" stroke-width="1.5" fill="none"/></svg></span></div>

<svg class="abs" style="left:568px;top:140px" width="590" height="590" viewBox="0 0 590 590">
  <path d="M24 265 A270 270 0 0 1 360 14" stroke="var(--yellow)" stroke-width="8" fill="none"/>
  <path d="M445 50 A270 270 0 0 1 120 540" stroke="var(--yellow)" stroke-width="8" fill="none"/>
</svg>
<div class="abs" role="img" aria-label="Photo of a robotic hand glowing in blue light" style="left:583px;top:152px;width:558px;height:558px;border-radius:50%;background:radial-gradient(circle at 55% 55%,#4fb3ff,#1b5fd6 45%,#0c8f9a 100%)"></div>

<!-- Services -->
<div class="abs serif kicker" style="top:830px">Lorum Ipsum</div>
<div class="abs serif title" style="top:862px">Our Services</div>
<p class="abs lead" style="top:925px">Lorem ipsum dolor sit amet, consectetur adipiscing elit. Quisque consectetur<br>non dolor ac fermentum. Sed vels odales metus, eu bibendum mi. Vivamus</p>

<div class="service" style="left:67px;top:1029px"><div class="ring"><div class="disc">
  <svg width="56" height="56" viewBox="0 0 56 56" fill="#fff"><rect x="6" y="36" width="7" height="14"/><rect x="17" y="30" width="7" height="20"/><rect x="28" y="24" width="7" height="26"/><rect x="39" y="18" width="7" height="32"/><path d="M6 30 L36 12 L33 8 L46 6 L42 18 L39 15 L8 34Z"/></svg>
</div></div><p>Service 1</p></div>
<div class="service" style="left:253px;top:1029px"><div class="ring"><div class="disc">
  <svg width="56" height="56" viewBox="0 0 56 56" fill="#fff"><rect x="22" y="12" width="28" height="22" rx="2"/><rect x="34" y="34" width="4" height="8"/><rect x="28" y="42" width="16" height="3"/><circle cx="13" cy="20" r="6"/><path d="M4 44 C4 32 22 32 22 44Z"/></svg>
</div></div><p>Service 2</p></div>
<div class="service" style="left:432px;top:1029px"><div class="ring"><div class="disc">
  <svg width="56" height="56" viewBox="0 0 56 56"><path d="M28 14a12 12 0 0 0-7 22v6h14v-6a12 12 0 0 0-7-22z" fill="none" stroke="#fff" stroke-width="3"/><rect x="22" y="44" width="12" height="3" fill="#fff"/><rect x="26.5" y="20" width="3" height="10" fill="#fff"/><circle cx="28" cy="33" r="2" fill="#fff"/><g stroke="#fff" stroke-width="2"><path d="M28 4v5M12 10l4 4M44 10l-4 4M6 26h5M45 26h5"/></g></svg>
</div></div><p>Service3</p></div>
<div class="service" style="left:615px;top:1029px"><div class="ring"><div class="disc">
  <svg width="56" height="56" viewBox="0 0 56 56" fill="#fff"><circle cx="14" cy="18" r="6"/><circle cx="42" cy="18" r="6"/><circle cx="28" cy="14" r="7"/><rect x="6" y="26" width="16" height="18" rx="5"/><rect x="34" y="26" width="16" height="18" rx="5"/><rect x="19" y="24" width="18" height="24" rx="5"/></svg>
</div></div><p>Service 4</p></div>
<div class="service" style="left:790px;top:1029px"><div class="ring"><div class="disc">
  <svg width="56" height="56" viewBox="0 0 56 56"><path d="M10 30a18 18 0 1 1 30 14v8H22v-6h-6v-8h-6z" fill="#fff"/><circle cx="30" cy="24" r="8" fill="none" stroke="var(--blue)" stroke-width="4" stroke-dasharray="4 2"/><circle cx="30" cy="24" r="3" fill="var(--blue)"/></svg>
</div></div><p>Service 5</p></div>
<div class="service" style="left:965px;top:1029px"><div class="ring"><div class="disc">
  <svg width="56" height="56" viewBox="0 0 56 56" fill="#fff"><path d="M14 26a14 14 0 0 1 28 0" fill="none" stroke="#fff" stroke-width="3"/><rect x="10" y="24" width="6" height="10" rx="2"/><rect x="40" y="24" width="6" height="10" rx="2"/><circle cx="28" cy="28" r="8"/><path d="M12 50c0-10 32-10 32 0Z"/></svg>
</div></div><p>Service 6</p></div>

<!-- About -->
<svg class="abs" style="left:0;top:1302px" width="1200" height="790" viewBox="0 0 1200 790" role="img" aria-label="Photo of a glowing aircraft cockpit instrument panel">
  <defs>
    <linearGradient id="cockpit" x1="0" y1="0" x2="1" y2="0.4">
      <stop offset="0" stop-color="#1b2430"/><stop offset="0.45" stop-color="#2a3a4c"/><stop offset="0.7" stop-color="#2f6b4a"/><stop offset="1" stop-color="#1a2a3a"/>
    </linearGradient>
  </defs>
  <path d="M0 0H1200V706C1050 650 900 660 760 700C560 760 330 800 0 710Z" fill="url(#cockpit)"/>
</svg>
<div class="abs" style="left:8px;top:1356px;width:694px;height:694px;border-radius:50%;background:rgba(200,200,200,.82)"></div>
<div class="abs" style="left:97px;top:1444px;width:518px;height:518px;border-radius:50%;background:var(--blue)"></div>
<div class="abs serif" style="left:97px;top:1578px;width:518px;text-align:center;font-size:32px;line-height:40px;color:var(--yellow)">About <span style="font-family:Poppins,sans-serif;font-weight:600;color:var(--white);font-size:26px">Quantel Brightforge</span></div>
<p class="abs" style="left:170px;top:1660px;width:372px;text-align:center;font-size:15px;line-height:26px;color:var(--white)">Lorem ipsum dolor sit amet, consefghctetur adipiscing elit, sed do eiusmod tempor inc ididunt ut labore et dolore magna aliqua. Ut</p>
<div class="abs btn btn-yellow" style="left:274px;top:1791px;width:189px;height:61px">Contact Us <span class="dot"><svg width="8" height="8" viewBox="0 0 8 8"><path d="M2 1l3 3-3 3" stroke="#fff" stroke-width="1.5" fill="none"/></svg></span></div>

<!-- Why choose -->
<div class="abs serif title" style="top:2208px">Why Choose <span style="font-family:Poppins,sans-serif;font-weight:600;font-size:40px">Quantel Brightforge</span>?</div>

<div class="reason" style="top:2365px"><div class="bulb"><svg width="40" height="48" viewBox="0 0 40 48"><path d="M20 10a11 11 0 0 0-6 20v6h12v-6a11 11 0 0 0-6-20z" fill="var(--yellow)" stroke="#333" stroke-width="1.5"/><rect x="15" y="38" width="10" height="5" fill="#555"/><g stroke="#999" stroke-width="1.5"><path d="M20 1v5M6 6l3 4M34 6l-3 4M1 20h5M34 20h5"/></g></svg></div><div><h3>Lorem ipsum dolor sit amet</h3><p>Seruned do eiusmodtempor incididunt ut<br>labore et dolore magnaaliquaUt.</p></div></div>
<div class="reason" style="top:2484px"><div class="bulb"><svg width="40" height="48" viewBox="0 0 40 48"><path d="M20 10a11 11 0 0 0-6 20v6h12v-6a11 11 0 0 0-6-20z" fill="var(--yellow)" stroke="#333" stroke-width="1.5"/><rect x="15" y="38" width="10" height="5" fill="#555"/><g stroke="#999" stroke-width="1.5"><path d="M20 1v5M6 6l3 4M34 6l-3 4M1 20h5M34 20h5"/></g></svg></div><div><h3>Lorem ipsum dolor sit amet</h3><p>Seruned do eiusmodtempor incididunt ut<br>labore et dolore magnaaliquaUt.</p></div></div>
<div class="reason" style="top:2607px"><div class="bulb"><svg width="40" height="48" viewBox="0 0 40 48"><path d="M20 10a11 11 0 0 0-6 20v6h12v-6a11 11 0 0 0-6-20z" fill="var(--yellow)" stroke="#333" stroke-width="1.5"/><rect x="15" y="38" width="10" height="5" fill="#555"/><g stroke="#999" stroke-width="1.5"><path d="M20 1v5M6 6l3 4M34 6l-3 4M1 20h5M34 20h5"/></g></svg></div><div><h3>Lorem ipsum dolor sit amet</h3><p>Seruned do eiusmodtempor incididunt ut<br>labore et dolore magnaaliquaUt.</p></div></div>
<div class="reason" style="top:2727px"><div class="bulb"><svg width="40" height="48" viewBox="0 0 40 48"><path d="M20 10a11 11 0 0 0-6 20v6h12v-6a11 11 0 0 0-6-20z" fill="var(--yellow)" stroke="#333" stroke-width="1.5"/><rect x="15" y="38" width="10" height="5" fill="#555"/><g stroke="#999" stroke-width="1.5"><path d="M20 1v5M6 6l3 4M34 6l-3 4M1 20h5M34 20h5"/></g></svg></div><div><h3>Lorem ipsum dolor sit amet</h3><p>Seruned do eiusmodtempor incididunt ut<br>labore et dolore magnaaliquaUt.</p></div></div>

<div class="abs" style="left:714px;top:2318px;width:444px;height:444px;border-radius:50%;background:var(--yellow)"></div>
<div class="abs" role="img" aria-label="Photo of a hand touching a futuristic holographic interface" style="left:694px;top:2318px;width:442px;height:442px;border-radius:50%;background:radial-gradient(circle at 40% 55%,#a39a94,#4a4a4e 45%,#1c1d22 100%)"></div>

<!-- Contact -->
<div class="abs" style="left:0;top:2939px;width:1200px;height:700px;background:var(--pale)"></div>
<div class="abs serif kicker" style="top:3028px">Get In&nbsp; Touch</div>
<div class="abs serif title" style="top:3056px">Contact <span style="font-family:Poppins,sans-serif;font-weight:600;font-size:40px">Quantel Brightforge</span></div>

<div class="info" style="top:3256px;align-items:flex-start"><span class="ic"><svg width="14" height="18" viewBox="0 0 14 18"><path d="M7 0a7 7 0 0 0-7 7c0 5 7 11 7 11s7-6 7-11a7 7 0 0 0-7-7z" fill="#fff"/><circle cx="7" cy="7" r="2.5" fill="var(--blue)"/></svg></span><span>Location Name<br>Dummy address here<br>Pin: 123456</span></div>
<div class="info" style="top:3335px"><span class="ic"><svg width="16" height="12" viewBox="0 0 16 12"><rect width="16" height="12" rx="1" fill="#fff"/><path d="M1 1l7 6 7-6" stroke="var(--blue)" stroke-width="1.4" fill="none"/></svg></span><span>Email:&nbsp; hello@quantelbrightforge.com</span></div>
<div class="info" style="top:3402px"><span class="ic"><svg width="16" height="16" viewBox="0 0 16 16"><path d="M3 1l3 3-2 2a9 9 0 0 0 6 6l2-2 3 3-2 2C7 15 1 9 1 3z" fill="#fff"/></svg></span><span>555 014 2210<br>555 019 8834</span></div>

<div class="field" style="left:593px;top:3244px">First Name*</div>
<div class="field" style="left:825px;top:3244px">Last Name</div>
<div class="rule" style="top:3277px"></div>
<div class="field" style="left:593px;top:3314px">Phone*</div>
<div class="field" style="left:825px;top:3314px">Email*</div>
<div class="rule" style="top:3347px"></div>
<div class="field" style="left:593px;top:3378px">Message*</div>
<div class="rule" style="top:3422px"></div>
<div class="abs btn btn-blue" style="left:758px;top:3478px;width:130px;height:51px">Submit <span class="dot"><svg width="8" height="8" viewBox="0 0 8 8"><path d="M2 1l3 3-3 3" stroke="#fff" stroke-width="1.5" fill="none"/></svg></span></div>

<!-- Footer -->
<svg class="abs" style="left:0;top:3560px" width="1200" height="305" viewBox="0 0 1200 305">
  <path d="M0 60 C150 20 330 40 480 90 C650 140 820 130 960 90 C1080 55 1150 30 1200 0 V305 H0Z" fill="var(--wave)"/>
  <path d="M0 95 C160 45 340 65 500 115 C660 165 830 160 980 110 C1090 75 1160 55 1200 40 V305 H0Z" fill="var(--blue)"/>
</svg>
<div class="abs brand" style="left:94px;top:3740px;width:220px;color:var(--white)">Quantel<br>Brightforge LLC</div>
<div class="foot">
  <a style="left:331px">Home</a><span class="sep" style="left:404px">|</span>
  <a style="left:428px">About us</a><span class="sep" style="left:523px">|</span>
  <a style="left:551px">Services</a><span class="sep" style="left:641px">|</span>
  <a style="left:671px">Blog</a><span class="sep" style="left:737px">|</span>
  <a style="left:763px">Contact Us</a>
</div>
<span class="social" style="left:947px"></span>
<span class="social" style="left:991px"></span>
<span class="social" style="left:1035px"></span>
<span class="social" style="left:1080px"></span>
<div class="abs" style="left:0;top:3861px;width:1200px;height:60px;background:var(--yellow);display:flex;align-items:center;justify-content:center;font-size:15px;color:#333">Copyright&nbsp; @&nbsp; 2023 All rights reserved</div>

</body>
</html>
```